Flyer-Design für Psychotherapeut
Zielgruppe
Angeboten wird als Dienstleistung Psychotherapie, Coaching und Paarberatung
für Einzelpersonen (Männer/Frauen), Paare und Familien in schwierigen privaten und beruflichen Lebenssituationen.
Aufgabenstellung
Sehr geehrte Damen, sehr geehrte Herren,
gewünscht wird ein Falzflyer Hochformat, DIN-Lang, Wickelfalz, 6 bedruckte Seiten mit dem Endformat 10,0 x 21,0 cm. Ein entsprechendes Datenblatt der Druckerei finden Sie im Anhang.
Der Flyer wird auf einer Gesundheitsmesse eingesetzt und soll einen Überblick über mein Dienstleistungsangebot geben.
In der beigefügten Word Datei finden Sie einen von mir erstellten Flyer-Text-Entwurf. Er soll lediglich als Orientierung dienen. Weitere Infos erhalten Sie auf meiner Homepage
www.praxis-tollring-quast.de.
Desweiteren erhalten Sie ein hochgeladenes Foto von mir, welches Sie bitte in Ihren Entwurf mit einbinden.
Ich bitte um Vorschläge für ein professionelles Design mit moderener gut lesbarer Schrift sowie farblich abgestimmten Blöcken des Inhalts.
Besonders wichtig ist mir die Orientierung an meinen Logofarben.
Das Logo wurde auch von gestaltwerk.de erstellt. Sie finden es unter meinen Projekten.
Für Rückfragen stehe ich Ihnen gerne zur Verfügung.
Freundliche Grüße
Sabine Tollring-Quast

```html
<!DOCTYPE html>
<html lang="de">
<head>
<meta charset="utf-8">
<title>Falzflyer – Sabine Tollring-Quast</title>
<link href="https://fonts.googleapis.com/css2?family=Open+Sans:wght@400;600;700&display=swap" rel="stylesheet">
<style>
:root{
  --orange:#e8531d;
  --orange-light:#f07a2e;
  --orange-deep:#d2440f;
  --ink:#4a4a4a;
  --ink-soft:#6b6b6b;
  --paper:#ffffff;
  --peach:#fbe3d3;
  --peach-soft:#fdf1e9;
  --stage:#2e2e2e;
  --band-grey:#b9b6b3;
}
*{box-sizing:border-box;margin:0;padding:0}
html,body{width:820px;height:1200px;overflow:hidden;background:var(--stage);font-family:"Open Sans",Arial,sans-serif;color:var(--ink)}
.sheet{position:absolute;left:22px;width:776px;background:var(--paper);overflow:hidden}
.sheet--outside{top:56px;height:560px}
.sheet--inside{top:642px;height:536px}
.panel{position:absolute;top:0;bottom:0;width:259px}
.panel--1{left:0}.panel--2{left:259px}.panel--3{left:518px}
.top-band{position:absolute;left:0;top:0;width:776px}
.top-band--outside{height:100px}
.top-band--inside{height:70px}
.photo{position:absolute}
h2{font-size:12.5px;font-weight:700;color:var(--orange);letter-spacing:.2px;line-height:1.2}
h3{font-size:8.2px;font-weight:600;color:var(--orange);text-transform:uppercase;line-height:1.35;margin-top:5px}
p{font-size:7px;line-height:1.45;color:var(--ink)}
.checklist{list-style:none;margin-top:7px}
.checklist li{position:relative;padding-left:13px;font-size:6.8px;line-height:1.4;margin-bottom:5px;color:var(--ink)}
.checklist li::before{content:"✔";position:absolute;left:0;top:-1px;color:var(--orange);font-size:8px}
.content{position:absolute;left:26px;right:18px}
/* outside */
.quote{position:absolute;left:300px;top:10px;width:200px;text-align:right;color:#fff;font-size:8px;font-weight:600;line-height:1.3}
.quote small{display:block;font-size:6px;font-weight:400;color:#fff;margin-top:2px}
.brand__dot{position:absolute;left:540px;top:20px;width:28px;height:28px;border-radius:50%;background:#fff;opacity:.9}
.brand__text{position:absolute;left:578px;top:20px;width:190px;color:#fff}
.brand__name{font-size:13px;font-weight:400;line-height:1.1;white-space:nowrap}
.brand__tag{font-size:6.5px;margin-top:4px;color:#fff;white-space:nowrap}
.contact-portrait{width:60px;height:60px;border-radius:6px;margin-top:10px}
.contact-name{font-size:7.5px;font-weight:700;color:var(--orange);margin-top:8px}
.badge{position:absolute;left:631px;top:333px;width:116px;height:116px;border-radius:50%;background:var(--orange);border:3px solid #fff;display:flex;flex-direction:column;justify-content:center;align-items:center;color:#fff;font-size:11px;font-weight:400;letter-spacing:.5px;transform:rotate(-18deg);line-height:1.45}
.badge .badge__line{border-bottom:1px solid #fff;padding-bottom:2px}
.claim{position:absolute;left:544px;top:502px;font-size:13px;color:var(--orange);line-height:1.45}
.url{position:absolute;left:0;width:241px;bottom:14px;text-align:right;font-size:7px;font-weight:700;color:var(--orange)}
/* inside */
.panel--3.inside-col{background:linear-gradient(180deg,var(--peach-soft),var(--peach))}
.grey-band{position:absolute;left:259px;top:28px;width:259px;height:30px;background:var(--band-grey);opacity:.55}
</style>
</head>
<body>

<section class="sheet sheet--outside">
  <svg class="top-band top-band--outside" viewBox="0 0 776 100" preserveAspectRatio="none" aria-hidden="true">
    <defs><linearGradient id="bandOut" x1="0" x2="1"><stop offset="0" stop-color="#f07a2e"/><stop offset="1" stop-color="#e04a14"/></linearGradient></defs>
    <path d="M0 0H776V100C620 70 480 54 330 50C200 46 90 36 0 24Z" fill="url(#bandOut)"/>
  </svg>

  <div class="photo" role="img" aria-label="Foto: Paar sitzt gemeinsam auf einer Treppe" style="left:0;top:24px;width:259px;height:172px;background:linear-gradient(135deg,#8aa0b8,#c9b9a8 55%,#7f9a5e)"></div>
  <div class="photo" role="img" aria-label="Foto: zwei Pfeile auf Asphalt vor einem Paar Schuhe" style="left:259px;top:44px;width:259px;height:152px;background:linear-gradient(160deg,#3a3a3a,#252525)"></div>
  <div class="photo" role="img" aria-label="Foto: steinerne Treppe im Grünen, die nach oben führt" style="left:518px;top:120px;width:258px;height:360px;background:linear-gradient(180deg,#8fa173,#9c7b5c 45%,#c8a886);clip-path:ellipse(150% 100% at 100% 100%)"></div>

  <svg style="position:absolute;left:0;top:190px" width="776" height="14" viewBox="0 0 776 14" aria-hidden="true"><path d="M0 14C200 0 380 2 518 8V14Z" fill="#fff"/></svg>

  <p class="quote">„Jeder Weg beginnt mit<br>dem ersten Schritt.“<small>(Alte Weisheit)</small></p>
  <span class="brand__dot"></span>
  <div class="brand__text"><div class="brand__name">Sabine Tollring-Quast</div><div class="brand__tag">Psychotherapie | Coaching | Paarberatung</div></div>

  <div class="panel panel--1">
    <div class="content" style="top:212px">
      <h2>PAARBERATUNG –</h2>
      <h3>Unterstützung für Paare<br>in Krisenzeiten</h3>
      <ul class="checklist">
        <li>Wenn Sie das Gefühl haben, einander verloren zu haben.</li>
        <li>Wenn Ihr Beziehungsalltag von Streitereien und Konflikten bestimmt wird.</li>
        <li>Wenn Sie Ihre gemeinsame Intimität und Sexualität verloren haben.</li>
        <li>Wenn eine Affäre Ihre Beziehung erschüttert hat.</li>
        <li>Wenn nach der Geburt von Kindern, durch Arbeitslosigkeit oder Krankheit Probleme in Ihrer Beziehung entstanden sind.</li>
        <li>Wenn das Leben in der Patchwork-Familie Ihre Beziehung belastet.</li>
      </ul>
      <h3 style="font-size:8.5px;margin-top:10px">Trennungsbegleitung und<br>Mediation</h3>
      <ul class="checklist"><li>Wenn Sie über Trennung nachdenken.</li></ul>
    </div>
  </div>

  <div class="panel panel--2">
    <div class="content" style="top:212px">
      <h2>HABEN SIE FRAGEN?</h2>
      <div class="contact-portrait" role="img" aria-label="Porträtfoto von Sabine Tollring-Quast" style="background:linear-gradient(135deg,#d9c9a0,#9a8f86)"></div>
      <p class="contact-name">SABINE TOLLRING-QUAST</p>
      <p>Heilpraktikerin Psychotherapie (HeilprG)<br>Systemischer Coach (VSCT)</p>
      <p style="margin-top:8px">Am Lindenhang 14<br>64290 Talbrück</p>
      <p style="margin-top:8px">Telefon 06150 - 472913<br>info@praxis-tollring-quast.de</p>
      <p style="margin-top:8px;color:var(--ink-soft)">Rufen Sie mich an. Ich bin für Sie da!<br>Ich freue mich auf Ihren Besuch.</p>
      <h3 style="font-size:8px;margin-top:22px">Weitere Informationen</h3>
      <p>über mich und meine Angebote finden<br>Sie auf meiner Homepage.</p>
    </div>
    <p class="url">www.praxis-tollring-quast.de</p>
  </div>

  <div class="badge"><span class="badge__line">AUSWEGE</span><span>LÖSUNGSWEGE</span></div>
  <p class="claim">Für mehr Zufriedenheit<br>im Privatleben und Beruf</p>
</section>

<section class="sheet sheet--inside">
  <div class="panel panel--3 inside-col"></div>
  <svg class="top-band top-band--inside" viewBox="0 0 776 70" preserveAspectRatio="none" aria-hidden="true">
    <defs><linearGradient id="bandIn" x1="0" x2="1"><stop offset="0" stop-color="#f07a2e"/><stop offset="1" stop-color="#d9460f"/></linearGradient></defs>
    <path d="M0 0H776V26C600 14 420 16 259 40C160 54 70 58 0 60Z" fill="url(#bandIn)"/>
  </svg>
  <div class="grey-band"></div>
  <div class="photo" role="img" aria-label="Foto: junge Frau am Schreibtisch mit einem Schild „Help“" style="left:0;top:52px;width:259px;height:138px;background:linear-gradient(135deg,#e9e4dc,#c8b9a6 50%,#f2efe9)"></div>

  <div class="panel panel--1">
    <div class="content" style="top:198px">
      <h2>SIE WÜNSCHEN SICH ...</h2>
      <h3>Entlastung und<br>positive Veränderung weil ...</h3>
      <ul class="checklist">
        <li>Sie sich in einer akuten privaten oder beruflichen Krisensituation befinden.</li>
        <li>Sie Probleme in Ihrer Partnerschaft haben.</li>
        <li>Sie mit Ihren Sorgen nicht allein sein wollen.</li>
        <li>Sie sich antriebslos und leer, erschöpft oder ständig überfordert fühlen.</li>
        <li>Sie unter Ängsten oder Panikattacken leiden, die Sie belasten und einschränken.</li>
      </ul>
      <p style="margin-top:26px">Jeder Mensch kommt im Leben in Situationen, die ihn aus dem Gleichgewicht bringen und die er nicht allein bewältigen möchte.</p>
      <p style="margin-top:8px">Wenn Veränderung nicht allein gelingt, können Psychotherapie, Coaching oder Paarberatung eine große Hilfe sein, um Lösungswege aus Ihrer belastenden Situation zu finden.</p>
    </div>
  </div>

  <div class="panel panel--2">
    <div class="content" style="top:78px">
      <h2>MEIN ANGEBOT FÜR SIE</h2>
      <h3>Beratung und Gespräche<br>Therapie nach Karl Roderich</h3>
      <h3>Systemisches Coaching und<br>Paarberatung</h3>
      <p style="margin-top:8px">Als erfahrene Therapeutin, Beraterin und Coach begleite ich Sie als Einzelperson, Paar oder Familie in schwierigen Lebensabschnitten und Veränderungsphasen.</p>
      <p style="margin-top:6px">Ich unterstütze Sie einfühlsam und lösungsorientiert. Dabei nutze ich anerkannte, wirksame Therapie- und Beratungsmethoden, die ich gemeinsam mit Ihnen auf Ihre persönlichen Bedürfnisse und Ziele abstimme.</p>
      <p style="margin-top:6px">Im Mittelpunkt stehen Sie mit Ihren Anliegen.</p>
      <p style="margin-top:6px">Wir begegnen uns in einer Atmosphäre der Wertschätzung, Annahme und absoluten Diskretion.</p>
      <h2 style="margin-top:18px">SIE KÖNNEN ...</h2>
      <ul class="checklist">
        <li>Bewältigungsstrategien entwickeln</li>
        <li>Ihre Fähigkeiten und Stärken entdecken</li>
        <li>Innere Blockaden überwinden</li>
        <li>Ihr Selbstvertrauen steigern</li>
        <li>Sich mutig und motiviert an Neues heranwagen</li>
        <li>Ihre Ziele umsetzen</li>
        <li>Ihr Leben und Ihre Partnerschaft so gestalten, wie Sie es sich wünschen.</li>
      </ul>
    </div>
  </div>

  <div class="panel panel--3">
    <div class="content" style="top:34px;left:22px">
      <h2>PSYCHOTHERAPIE</h2>
      <h3 style="margin-top:8px">Meine Behandlungsschwerpunkte</h3>
      <ul class="checklist">
        <li>Ängste und Panikattacken</li>
        <li>Depression</li>
        <li>Erschöpfung / Burnout</li>
        <li>Reaktion auf schwere Belastungen</li>
        <li>Psychosomatische Beschwerden</li>
        <li>Psychoonkologie</li>
        <li>Berufliche Gesundheitsberatung</li>
      </ul>
      <h2 style="margin-top:12px">COACHING</h2>
      <h3>Begleitung in Veränderungsprozessen und schwierigen Lebensphasen / -krisen</h3>
      <ul class="checklist">
        <li>Veränderte Rahmenbedingungen im Privat- und Berufsleben wie z.B. Krankheit, Trennung, Trauer, Mobbing, Arbeitsplatzverlust u.a.</li>
        <li>Berufliche Neuorientierung</li>
        <li>Entscheidungsfindung</li>
        <li>Zielsetzung und Realisierung</li>
        <li>Lebensumbrüche wie z.B. Wechseljahre, Pensionierung u.a.</li>
      </ul>
      <h3 style="font-size:8.5px;margin-top:8px">Persönlichkeitsentwicklung</h3>
      <ul class="checklist">
        <li>Konflikte erkennen und konstruktiv lösen</li>
        <li>Beziehungs- und Lebensgestaltung</li>
        <li>Eigene Stärken entdecken, weiter entwickeln und nutzen</li>
        <li>Stressbewältigung / Burnoutprävention</li>
      </ul>
    </div>
  </div>
</section>

</body>
</html>
```